Midnight Lanterns - Falling to Rise Reading the Hidden Grammar of Sleep

Book Title:
Midnight Lanterns
Falling to Rise

Reading the Hidden Grammar of Sleep

by Greta Vonhalm

tells the story of how dreams transform us, bringing the wisdom of our mind, body and spirit to us in our dreams. We have nerves coming into our brain from every part of our body relaying psychological and physiological information within us and it is revealed in our dream narrative.Once you understand the symbolic, visual language of dreams, you will find out/understand what is going on within. After all the dream is always about the dreamer. Yes, it is all about you!

Target Market(s)

Anyone who dreams, that includes all of us

Font styles to use
Serif

Colors
ec1f27
f37122
0692cd

Requirements
Must have
• Use this image please with Shadowed serif type font, in the color pallette
• I would like images for the cover to reflect being reborn for example - a phoenix. Dying in a dream is always a symbolic gesture/metaphor of profound psychological spiritual change, and the way the person dies is symbolic too. It's important that the image on the front reflects that.
Nice to have
• A good visual on the cover helps, just like they do in a dream since the language of the dream is symbols, metaphor, colors portray emotions. We respond to images because we only had images before our written language

```html
<!DOCTYPE html>
<html lang="en">
<head>
<meta charset="utf-8">
<title>Midnight Lanterns – Falling to Rise</title>
<link rel="stylesheet" href="https://fonts.googleapis.com/css2?family=Cinzel:wght@400;600;700&family=Cormorant+SC:wght@500;600&display=swap">
<style>
  :root {
    --crimson: #ec1f27;
    --deep-red: #8e0c12;
    --wine: #5a060a;
    --ember: #f37122;
    --flame: #ffd36a;
    --core: #fff1c4;
    --sky: #0692cd;
    --sky-light: #7fd3f5;
    --sky-deep: #04618a;
    --silver: #e9e6ea;
    --shadow: rgba(30, 0, 4, 0.85);
  }
  html, body {
    margin: 0;
    padding: 0;
    width: 750px;
    height: 1200px;
    overflow: hidden;
    background: var(--wine);
  }
  .cover {
    position: relative;
    width: 750px;
    height: 1200px;
    overflow: hidden;
    background:
      radial-gradient(ellipse 60% 45% at 50% 58%, rgba(236, 31, 39, 0.9) 0%, rgba(236, 31, 39, 0) 70%),
      radial-gradient(ellipse 80% 60% at 30% 20%, rgba(210, 30, 40, 0.6) 0%, rgba(0, 0, 0, 0) 70%),
      linear-gradient(180deg, var(--deep-red) 0%, #b5141b 40%, #a3121a 70%, var(--wine) 100%);
    font-family: "Cinzel", "Times New Roman", serif;
    text-align: center;
  }
  .phoenix-art {
    position: absolute;
    left: 0;
    top: 340px;
    width: 750px;
    height: 860px;
  }
  .title {
    position: absolute;
    top: 16px;
    left: 0;
    width: 100%;
    margin: 0;
    font-weight: 700;
    line-height: 1;
    color: var(--sky);
    z-index: 1;
  }
  .title-top,
  .title-main {
    display: block;
    background: linear-gradient(180deg, var(--sky-light) 0%, var(--sky) 55%, var(--sky-deep) 100%);
    -webkit-background-clip: text;
    background-clip: text;
    -webkit-text-fill-color: transparent;
    filter: drop-shadow(3px 4px 3px var(--shadow));
  }
  .title-top {
    font-size: 82px;
    letter-spacing: 2px;
  }
  .title-main {
    margin-top: 2px;
    font-size: 122px;
    letter-spacing: 0;
  }
  .tagline {
    position: absolute;
    top: 262px;
    left: 0;
    width: 100%;
    margin: 0;
    font-size: 38px;
    font-weight: 600;
    letter-spacing: 6px;
    color: var(--silver);
    text-shadow: 2px 3px 3px var(--shadow);
    z-index: 1;
  }
  .subtitle {
    position: absolute;
    top: 312px;
    left: 0;
    width: 100%;
    margin: 0;
    font-family: "Cormorant SC", "Times New Roman", serif;
    font-size: 15px;
    font-weight: 600;
    letter-spacing: 1.5px;
    color: var(--silver);
    text-shadow: 1px 1px 2px var(--shadow);
    z-index: 1;
  }
  .author {
    position: absolute;
    bottom: 40px;
    left: 0;
    width: 100%;
    margin: 0;
    font-size: 42px;
    font-weight: 700;
    letter-spacing: 2px;
    background: linear-gradient(180deg, var(--sky-light) 0%, var(--sky) 60%, var(--sky-deep) 100%);
    -webkit-background-clip: text;
    background-clip: text;
    -webkit-text-fill-color: transparent;
    filter: drop-shadow(2px 3px 2px var(--shadow));
    z-index: 1;
  }
</style>
</head>
<body>
  <main class="cover">
    <svg class="phoenix-art" viewBox="0 0 750 860" role="img" aria-label="Illustration of a blazing phoenix rising from the flames, head raised and wings of fire spread across the cover, its tail trailing down behind the author name">
      <defs>
        <radialGradient id="phoenix-glow" cx="50%" cy="42%" r="50%">
          <stop offset="0%" stop-color="#fff1c4"/>
          <stop offset="18%" stop-color="#ffd36a"/>
          <stop offset="45%" stop-color="#f37122" stop-opacity="0.9"/>
          <stop offset="75%" stop-color="#ec1f27" stop-opacity="0.45"/>
          <stop offset="100%" stop-color="#ec1f27" stop-opacity="0"/>
        </radialGradient>
      </defs>
      <ellipse cx="375" cy="380" rx="400" ry="420" fill="url(#phoenix-glow)"/>
    </svg>

    <h1 class="title">
      <span class="title-top">MIDNIGHT</span>
      <span class="title-main">LANTERNS</span>
    </h1>
    <p class="tagline">FALLING TO RISE</p>
    <p class="subtitle">READING THE HIDDEN GRAMMAR OF SLEEP</p>

    <p class="author">GRETA VONHALM</p>
  </main>
</body>
</html>
```